Electrical Business Card Design

New electrical business targeting my local area
Installations
Repairs
Switchboards
TV / Vistacast / Antennas
Telephone
Data Networks
Audio Visual
Licence # 518247K
ABN 63918257041
I would like some white background, black writing, red, blue & green can be used
Designer discretion to be used on layout, colour placement & any images
Updates
Project Deadline Extended
Reason: To give designers more time, I thought 5 days wasn't enough
Please don't just create generic business cards................include personal details e.g. business name, contact name, ph #, email. Also include the things I do, licence # & abn (refer to brief for all details)
Thanks
Project Deadline Extended
Reason: Would like more designs & have now committed my payment, thank you
Industry/Entity Type
Electrical
Contact Information for Business Card
Korvale Electrical Services,
Derek Halloran,
0498 351 672,
korvaleelectrical@plumnet.net.au,
My suburb is Ryde
Look and feel

```html
<!DOCTYPE html>
<html lang="en">
<head>
<meta charset="utf-8">
<title>Korvale Electrical Services – Business Card</title>
<link href="https://fonts.googleapis.com/css2?family=Lato:wght@400;700;900&display=swap" rel="stylesheet">
<style>
  :root {
    --bg: #1c1c1e;
    --card: #ffffff;
    --ink: #111111;
    --green: #3aa876;
    --blue: #1f4384;
    --divider: #2a4a86;
  }
  * { box-sizing: border-box; margin: 0; padding: 0; }
  html, body {
    width: 1200px; height: 926px; overflow: hidden;
    background: var(--bg);
    font-family: "Lato", Arial, sans-serif;
    color: var(--ink);
  }
  .canvas {
    width: 1200px; height: 926px;
    display: flex; flex-direction: column;
    align-items: center; justify-content: center; gap: 50px;
  }
  .card {
    position: relative;
    width: 660px; height: 403px;
    background: var(--card);
    overflow: hidden;
  }
  .card__waves { position: absolute; inset: 0; width: 100%; height: 100%; }

  /* Front */
  .front__company {
    position: absolute; top: 62px; left: 0; right: 0;
    text-align: center;
    font-weight: 900; font-size: 29px; letter-spacing: 0.3px;
    text-transform: uppercase;
  }
  .front__name {
    position: absolute; top: 128px; left: 196px;
    font-size: 31px; font-weight: 400;
  }
  .front__name strong { font-weight: 700; }
  .front__details {
    position: absolute; top: 182px; left: 40px;
    display: flex; align-items: stretch; gap: 14px;
    font-size: 15px; line-height: 1.45;
  }
  .front__ids { font-weight: 700; }
  .front__divider { width: 2px; background: var(--divider); }
  .front__contact dt { font-weight: 700; display: inline-block; width: 14px; }
  .front__contact dd { display: inline; }
  .front__contact div { white-space: nowrap; }

  /* Back */
  .services {
    position: absolute; list-style: none;
    font-size: 19px; letter-spacing: 0.6px; line-height: 1.35;
  }
  .services li { display: flex; align-items: center; gap: 12px; }
  .services li::before {
    content: ""; width: 13px; height: 13px; background: var(--green); flex: none;
  }
  .services--primary { top: 78px; left: 80px; }
  .services--secondary { top: 188px; left: 392px; }
</style>
</head>
<body>
<main class="canvas">
  <section class="card card--front" aria-label="Business card front">
    <svg class="card__waves" viewBox="0 0 660 403" preserveAspectRatio="none" aria-hidden="true">
      <path fill="var(--green)" d="M0 220 C 60 250, 110 320, 260 340 C 400 358, 560 345, 660 345 L660 403 L0 403 Z"/>
      <path fill="#ffffff" d="M0 268 C 80 300, 160 340, 300 352 C 440 362, 570 360, 660 362 L660 403 L0 403 Z"/>
      <path fill="var(--blue)" d="M0 274 C 80 306, 160 344, 300 357 C 440 367, 570 366, 660 368 L660 403 L0 403 Z"/>
    </svg>
    <h1 class="front__company">Korvale Electrical Services</h1>
    <p class="front__name">Derek <strong>Halloran</strong></p>
    <div class="front__details">
      <div class="front__ids">
        <div>Licence # 518247K</div>
        <div>ABN 63918257041</div>
      </div>
      <span class="front__divider"></span>
      <dl class="front__contact">
        <div><dt>P</dt><dd>: 0498 351 672</dd></div>
        <div><dt>E</dt><dd>: korvaleelectrical@plumnet.net.au</dd></div>
      </dl>
    </div>
  </section>

  <section class="card card--back" aria-label="Business card back">
    <ul class="services services--primary">
      <li>New installations</li>
      <li>Repairs &amp; additions</li>
      <li>TV/Vistacast/Antennas</li>
    </ul>
    <ul class="services services--secondary">
      <li>Phone Systems</li>
      <li>Data Networks</li>
      <li>Audio Visual</li>
    </ul>
  </section>
</main>
</body>
</html>
```